Website Design For Ecommerce Brand That Sells Personalized Wall Decor

We need a new website for our company Copper Lantern. Our current site is functioning through wordpress/woocomerce but we are not happy with the appearance. Our products really wow people when they receive them and we need your help making our website do the same!

Number of Pages Required

4 page

```html
<!DOCTYPE html>
<html lang="en">
<head>
<meta charset="utf-8">
<title>Copper Lantern – Personalized Wall Decor</title>
<link href="https://fonts.googleapis.com/css2?family=Playfair+Display:wght@400;500;600&family=Poppins:ital,wght@0,300;0,400;0,500;0,600;1,300;1,400&display=swap" rel="stylesheet">
<style>
:root{
  --green:#6b9a58;
  --green-dark:#4f8a3d;
  --ink:#1b1b1b;
  --muted:#666;
  --line:#e6e6e6;
  --star:#f2b01e;
  --dark:#121212;
  --white:#fff;
}
*{box-sizing:border-box;margin:0;padding:0}
html,body{width:1200px;height:4435px;overflow:hidden}
body{position:relative;font-family:"Poppins",sans-serif;color:var(--ink);background:var(--white)}
.abs{position:absolute}

/* top bar */
.topbar{left:0;top:0;width:1200px;height:38px;background:var(--green);color:#fff;font-size:13px;display:flex;align-items:center;justify-content:space-between;padding:0 78px 0 100px}
.topbar span{display:flex;align-items:center;gap:8px}
.header{left:0;top:38px;width:1200px;height:72px;border-bottom:1px solid var(--line)}
.search{left:100px;top:55px;width:313px;height:40px;border-radius:20px;background:#f1f1f1;display:flex;align-items:center;font-size:11px;color:#777;padding-left:22px}
.search .cat{margin-left:auto;margin-right:14px}
.search .go{width:52px;height:40px;border-radius:20px;background:var(--green);display:flex;align-items:center;justify-content:center}
.icons{left:977px;top:58px;display:flex;gap:18px}
.nav{left:0;top:110px;width:1200px;height:52px;font-size:14px;font-weight:500}
.nav a{position:absolute;top:16px;color:var(--ink);text-decoration:none}
.nav a.active{color:var(--green)}
.logo{left:488px;top:-30px;width:224px;height:232px;border-radius:50%;background:#fff;box-shadow:0 2px 6px rgba(0,0,0,.12);display:flex;flex-direction:column;align-items:center;justify-content:center;padding-top:40px;z-index:3}
.logo .dot{width:44px;height:44px;border-radius:50%;background:var(--ink);margin-bottom:8px}
.logo .name{font-weight:600;font-size:27px;line-height:1.05;letter-spacing:2px;text-align:center;color:var(--ink)}

/* hero */
.hero{left:0;top:162px;width:1200px;height:625px;background:linear-gradient(100deg,#2b1a12 0%,#5c3a27 35%,#7a5038 60%,#4a2e20 100%)}
.hero-title{left:668px;top:340px;color:#fff;font-family:"Playfair Display",serif;font-size:58px;font-weight:500;line-height:1.07;white-space:nowrap;text-shadow:0 2px 6px rgba(0,0,0,.35)}
.btn{display:inline-flex;align-items:center;gap:6px;background:var(--green);color:#fff;font-size:14px;font-weight:500;border-radius:22px;padding:0 26px;height:42px;text-decoration:none}
.arrow{width:20px;height:34px}
.dots{left:560px;top:738px;display:flex;gap:12px}
.dots i{width:12px;height:12px;border:1.5px solid #fff;border-radius:50%;display:block}
.dots i.on{background:#fff}

/* section titles */
.title{left:0;width:1200px;text-align:center;font-family:"Playfair Display",serif;font-size:46px;font-weight:500;color:var(--ink)}
.rule{left:540px;width:120px;height:2px;background:linear-gradient(90deg,transparent,var(--green),transparent)}

/* product cards */
.card{background:#fff;box-shadow:0 2px 10px rgba(0,0,0,.07);text-align:center}
.card .ph{width:100%}
.stars{color:var(--star);font-size:13px;letter-spacing:1px}
.stars small{color:#555;font-size:11px;letter-spacing:0;margin-left:4px}
.card h3{font-weight:400;font-size:18px;line-height:1.25;margin:10px 14px 6px}
.card .price{color:var(--green-dark);font-size:20px}
.arrivals .card{position:absolute;width:317px;height:396px}
.arrivals .ph{height:263px}
.arrivals .stars{margin-top:18px}
.picked .card{position:absolute;width:239px;height:342px;top:2605px}
.picked .ph{height:206px}
.picked .stars{margin-top:20px}
.picked h3{font-size:16px;margin:8px 10px 4px}
.picked .price{font-size:19px}

/* banner */
.banner{left:0;top:1868px;width:1200px;height:499px;background:linear-gradient(180deg,#c9ccd0 0%,#aeb2b6 60%,#7a5a43 80%,#5e4130 100%)}
.banner-art{left:72px;top:1965px;width:550px;height:280px;background:linear-gradient(135deg,#eadcc6,#c9b396)}
.promo{left:683px;top:1952px;width:405px;height:331px;background:#fff;border-radius:6px;padding:28px 28px}
.promo h2{font-family:"Playfair Display",serif;font-weight:500;font-size:44px;line-height:1.12}
.promo p{font-size:17px;line-height:30px;margin:16px 0 18px;color:#222}

/* tabs */
.tabs{left:0;top:2540px;width:1200px;display:flex;justify-content:center;align-items:center;gap:28px;font-size:13px;font-weight:500}
.tabs .all{background:var(--green);color:#fff;border-radius:14px;padding:3px 22px}

/* testimonials */
.quote{position:absolute;top:3240px;width:480px;height:300px;background:#fff;box-shadow:0 2px 12px rgba(0,0,0,.08);padding:26px 28px}
.quote .qm{font-family:"Playfair Display",serif;color:var(--green);font-size:80px;line-height:.8;font-weight:600;height:40px}
.quote .stars{position:absolute;right:22px;top:30px;font-size:22px;letter-spacing:2px}
.quote p{font-style:italic;font-weight:300;font-size:15px;line-height:27px;color:#444;margin-top:12px}
.person{display:flex;align-items:center;gap:14px;margin-top:12px}
.avatar{width:54px;height:54px;border-radius:50%;background:linear-gradient(#d9c2ae,#a98b72)}
.person b{display:block;color:var(--green);font-weight:400;font-size:17px}
.person small{font-size:11px;color:#444}

/* newsletter */
.news{left:0;top:3628px;width:1200px;height:332px;background:var(--green)}
.news-art{left:95px;top:3645px;width:425px;height:315px;background:linear-gradient(160deg,#3d5260 0%,#7d6a58 50%,#2e2e2e 100%)}
.news h2{position:absolute;left:616px;top:82px;color:#fff;font-family:"Playfair Display",serif;font-weight:500;font-size:38px}
.news p{position:absolute;left:616px;top:132px;color:#fff;font-size:13px}
.signup{position:absolute;left:611px;top:168px;width:489px;height:66px;border-radius:33px;background:#fff;display:flex;align-items:center;padding-left:28px;font-size:13px;color:#666}
.signup .btn{margin-left:auto;height:58px;margin-right:4px;border-radius:29px;padding:0 40px;font-size:16px;font-weight:600;background:var(--green-dark)}

/* features */
.features{left:0;top:3960px;width:1200px;height:120px;background:var(--dark);color:#fff;display:flex;align-items:center;justify-content:space-around;padding:0 20px}
.feat{display:flex;align-items:center;gap:10px;font-size:12px;line-height:1.2;padding:0 24px;border-right:1px solid #444}
.feat:last-child{border-right:0}
.feat b{display:block;font-size:14px;font-weight:600}

/* footer */
.footer{left:0;top:4080px;width:1200px;height:355px;background:var(--dark);color:#fff}
.col{position:absolute;top:35px;font-size:13px}
.col h4{font-size:16px;font-weight:500;margin-bottom:16px}
.col li{list-style:none;line-height:29px}
.col p{font-size:11px;line-height:21px;color:#ddd}
.mail{width:205px;height:40px;border-radius:20px;background:#fff;color:#777;font-size:12px;display:flex;align-items:center;padding-left:10px;margin-top:10px}
.mail i{margin-left:auto;margin-right:4px;width:32px;height:32px;border-radius:50%;background:var(--green)}
.socials{display:flex;gap:10px;margin-top:18px}
.socials i{width:42px;height:42px;border-radius:50%;border:1.5px solid #fff;display:block}
.copy{position:absolute;left:120px;top:318px;font-size:13px}
.pay{position:absolute;left:795px;top:312px;display:flex;gap:14px}
.pay i{width:42px;height:22px;border-radius:3px;background:#3b4a8c;display:block}
</style>
</head>
<body>

<div class="abs topbar">
  <span><svg width="14" height="14" viewBox="0 0 24 24" fill="#fff"><path d="M6.6 10.8a15 15 0 0 0 6.6 6.6l2.2-2.2c.3-.3.7-.4 1-.2 1.1.4 2.3.6 3.6.6.6 0 1 .4 1 1V20c0 .6-.4 1-1 1A17 17 0 0 1 3 4c0-.6.4-1 1-1h3.5c.6 0 1 .4 1 1 0 1.3.2 2.5.6 3.6.1.3 0 .7-.2 1z"/></svg>Call Now! to Redeem Huge Deals! 123-456-7890</span>
  <span><svg width="14" height="12" viewBox="0 0 24 18" fill="#fff"><path d="M0 0h24v18H0z" opacity=".9"/><path d="M0 0l12 9 12-9" stroke="#6b9a58" stroke-width="2" fill="none"/></svg>Support@Copperlantern.Com</span>
</div>

<div class="abs header"></div>
<div class="abs search">Search...<span class="cat">All Categories ▾</span><span class="go"><svg width="20" height="20" viewBox="0 0 24 24" fill="none" stroke="#fff" stroke-width="2"><circle cx="10" cy="10" r="7"/><path d="M15 15l6 6"/></svg></span></div>
<div class="abs icons">
  <svg width="30" height="30" viewBox="0 0 24 24" fill="none" stroke="#222" stroke-width="1.5"><circle cx="12" cy="8" r="4"/><path d="M4 21c1-5 15-5 16 0"/></svg>
  <svg width="30" height="30" viewBox="0 0 24 24" fill="none" stroke="#222" stroke-width="1.5"><path d="M12 20s-8-5-8-11a4 4 0 0 1 8-1 4 4 0 0 1 8 1c0 6-8 11-8 11z"/></svg>
  <svg width="36" height="30" viewBox="0 0 30 24" fill="none" stroke="#222" stroke-width="1.5"><path d="M3 8h16l-1 14H4z"/><path d="M7 8a4 4 0 0 1 8 0"/><circle cx="22" cy="6" r="5" fill="#6b9a58" stroke="none"/><text x="22" y="8.5" font-size="7" fill="#fff" stroke="none" text-anchor="middle" font-family="Poppins">0</text></svg>
</div>

<nav class="abs nav">
  <a class="active" style="left:100px">HOME</a>
  <a style="left:211px">ABOUT US</a>
  <a style="left:361px">PRODUCTS</a>
  <a style="left:759px">SHOP</a>
  <a style="left:883px">FAQ</a>
  <a style="left:999px">CONTACT US</a>
</nav>

<div class="abs logo"><span class="dot"></span><span class="name">COPPER<br>LANTERN</span></div>

<section class="abs hero" role="img" aria-label="Personalized wooden name ornament with a dinosaur cut-out on a rustic wood table with holiday decorations"></section>
<h1 class="abs hero-title">Welcome To<br>Copper Lantern!</h1>
<a class="abs btn" style="left:671px;top:506px">SHOP NOW <svg width="14" height="12" viewBox="0 0 24 20" fill="#fff"><path d="M0 0h4l1 3h19l-3 9H7l1 2h14v2H7L3 2H0z"/></svg></a>
<svg class="abs arrow" style="left:64px;top:455px" viewBox="0 0 20 34" fill="none" stroke="#fff" stroke-width="2"><path d="M18 2L3 17l15 15"/></svg>
<svg class="abs arrow" style="left:1112px;top:455px" viewBox="0 0 20 34" fill="none" stroke="#fff" stroke-width="2"><path d="M2 2l15 15L2 32"/></svg>
<div class="abs dots"><i></i><i class="on"></i><i></i><i></i></div>

<!-- New arrivals -->
<h2 class="abs title" style="top:862px">New Arrivals</h2>
<div class="abs rule" style="top:926px"></div>
<div class="arrivals">
  <article class="card" style="left:100px;top:959px"><div class="ph" role="img" aria-label="Pet memorial paw print ornament" style="background:linear-gradient(135deg,#6b1c1c,#8a6a55 60%,#c9ad8e)"></div><div class="stars">★★★★★<small>(42 reviews)</small></div><h3>In Memory of Lost Pet Ornament</h3><div class="price">$16.00</div></article>
  <article class="card" style="left:441px;top:959px"><div class="ph" role="img" aria-label="Framed grandkids family tree sign" style="background:linear-gradient(135deg,#3e3a36,#8c8376 50%,#d8d2c8)"></div><div class="stars">★★★★★<small>(42 reviews)</small></div><h3>12 Inch Square Framed Personalized Family Tree</h3><div class="price">$16.00</div></article>
  <article class="card" style="left:782px;top:959px"><div class="ph" role="img" aria-label="Pet memorial plaque on a wooden stand" style="background:linear-gradient(135deg,#b9a68f,#e6dccd 50%,#c3b7a6)"></div><div class="stars">★★★★★<small>(42 reviews)</small></div><h3>In Memory of Lost Pet Plaque, Custom Memorial Sign</h3><div class="price">$16.00</div></article>
  <article class="card" style="left:100px;top:1377px"><div class="ph" role="img" aria-label="Grandkids ornament with name tags" style="background:linear-gradient(135deg,#5b1b1b,#6b4a36 45%,#c9ad8e)"></div><div class="stars">★★★★★<small>(42 reviews)</small></div><h3>In Memory of Lost Pet Ornament</h3><div class="price">$16.00</div></article>
  <article class="card" style="left:441px;top:1377px"><div class="ph" role="img" aria-label="Faux shiplap family tree sign" style="background:linear-gradient(135deg,#d9d4cc,#b8aa95 55%,#9b8a75)"></div><div class="stars">★★★★★<small>(42 reviews)</small></div><h3>Faux Shiplap Personalized Family Tree</h3><div class="price">$16.00</div></article>
  <article class="card" style="left:782px;top:1377px"><div class="ph" role="img" aria-label="Unfinished wooden pumpkin cut-out" style="background:linear-gradient(135deg,#6d6a66,#a89e92 50%,#7a736b)"></div><div class="stars">★★★★★<small>(42 reviews)</small></div><h3>Pumpkin – Interchangeable Piece For Gnome Kit...</h3><div class="price">$16.00</div></article>
</div>

<!-- Banner -->
<section class="abs banner" role="img" aria-label="Grey wall and wooden floor backdrop"></section>
<div class="abs banner-art" role="img" aria-label="Shiplap family tree sign with engraved script"></div>
<div class="abs promo">
  <h2>Personalize the Family Tree</h2>
  <p>Lorem ipsum dolor s amet, consectetur adipiscing elit, sed do eiusmod tempor incididunt ut labore</p>
  <span class="btn">SHOP NOW <svg width="14" height="12" viewBox="0 0 24 20" fill="#fff"><path d="M0 0h4l1 3h19l-3 9H7l1 2h14v2H7L3 2H0z"/></svg></span>
</div>

<!-- Top picked -->
<h2 class="abs title" style="top:2443px">Tops Picked Products</h2>
<div class="abs rule" style="top:2508px"></div>
<div class="abs tabs"><span class="all">ALL</span><span>HOME DECOR</span><span>GNOME</span><span>CRAFT SUPPLIES</span><span>PRE-CUT SHAPES</span><span>UNFINISHED WOOD</span><span>HALLOWEEN</span></div>
<div class="picked">
  <article class="card" style="left:100px"><div class="ph" role="img" aria-label="Together they built a life wooden sign" style="background:linear-gradient(135deg,#e3b59b,#d9d3c9 50%,#b7a998)"></div><div class="stars">★★★★★<small>(42 reviews)</small></div><h3>Together They Built-06</h3><div class="price">$16.00</div></article>
  <article class="card" style="left:353px"><div class="ph" role="img" aria-label="Blank wooden gnome with sunflower" style="background:linear-gradient(135deg,#3a2a20,#d8d1c6 50%,#4a3325)"></div><div class="stars">★★★★★<small>(42 reviews)</small></div><h3>Gnome with Sunflower-blank</h3><div class="price">$16.00</div></article>
  <article class="card" style="left:608px"><div class="ph" role="img" aria-label="Hexagon name ornament with dinosaur" style="background:linear-gradient(135deg,#4b2c1e,#c7a47f 50%,#5b3a28)"></div><div class="stars">★★★★★<small>(42 reviews)</small></div><h3>In Memory of Lost Pet Ornament</h3><div class="price">$16.00</div></article>
  <article class="card" style="left:861px"><div class="ph" role="img" aria-label="Faux shiplap family tree sign" style="background:linear-gradient(135deg,#c8c4bc,#d9cbb5 55%,#8a6e52)"></div><div class="stars">★★★★★<small>(42 reviews)</small></div><h3>Faux Shiplap Personalized Family Tree</h3><div class="price">$16.00</div></article>
</div>
<svg class="abs arrow" style="left:62px;top:2757px" viewBox="0 0 20 34" fill="none" stroke="#333" stroke-width="2"><path d="M18 2L3 17l15 15"/></svg>
<svg class="abs arrow" style="left:1110px;top:2757px" viewBox="0 0 20 34" fill="none" stroke="#333" stroke-width="2"><path d="M2 2l15 15L2 32"/></svg>

<!-- Testimonials -->
<h2 class="abs title" style="top:3108px">What Our happy Clients Say</h2>
<div class="abs rule" style="top:3172px"></div>
<article class="quote" style="left:105px"><div class="qm">“</div><div class="stars">★★★★★</div><p>Sed ut perspiciatis unde omnis natus error sit voluptatem accusantium doloremque laudtium, totam rem aperiam, eaque ipsa quae ab illo inve veritatis et quasi architecto beatae vitae dicta suabo. Nemo enim ipsam voluptatem quia voluptas sit aspernatur</p><div class="person"><span class="avatar" role="img" aria-label="Client portrait"></span><div><b>Nora Vale</b><small>Sed ut perspiciatis</small></div></div></article>
<article class="quote" style="left:613px"><div class="qm">“</div><div class="stars">★★★★★</div><p>Sed ut perspiciatis unde omnis natus error sit voluptatem accusantium doloremque laudtium, totam rem aperiam, eaque ipsa quae ab illo inve veritatis et quasi architecto beatae vitae dicta suabo. Nemo enim ipsam voluptatem quia voluptas sit aspernatur</p><div class="person"><span class="avatar" role="img" aria-label="Client portrait"></span><div><b>Nora Vale</b><small>Sed ut perspiciatis</small></div></div></article>

<!-- Newsletter -->
<section class="abs news">
  <h2>Subscribe to our Newsletter</h2>
  <p>A short sentence describing what someone will receive by subscribing</p>
  <div class="signup">Enter Your Email Address<span class="btn">SUBSCRIBE</span></div>
</section>
<div class="abs news-art" role="img" aria-label="Tiered tray with seasonal wooden decor pieces"></div>

<!-- Features -->
<section class="abs features">
  <div class="feat"><svg width="40" height="26" viewBox="0 0 40 26" fill="none" stroke="#fff" stroke-width="1.6"><path d="M8 4h18v14H8zM26 9h7l4 5v4h-11"/><circle cx="13" cy="20" r="3"/><circle cx="31" cy="20" r="3"/></svg><div><b>FAST SHIPPING</b>Deliveries throughout Italy</div></div>
  <div class="feat"><svg width="30" height="30" viewBox="0 0 24 24" fill="none" stroke="#fff" stroke-width="1.6"><path d="M4 14v-2a8 8 0 0 1 16 0v2"/><rect x="3" y="13" width="4" height="6" rx="1"/><rect x="17" y="13" width="4" height="6" rx="1"/></svg><div><b>CUSTOMER SERVICE</b>From9:00 to 13:00 &nbsp;☏ 888 888 8888</div></div>
  <div class="feat"><svg width="30" height="30" viewBox="0 0 24 24" fill="none" stroke="#fff" stroke-width="1.6"><rect x="3" y="3" width="14" height="18"/><path d="M6 8h8M6 12h8M6 16h4"/><circle cx="18" cy="17" r="3"/></svg><div><b>CERTIFIED PRODUCTS</b>Guaranteed, of quality and in<br>accordance with the law</div></div>
  <div class="feat"><svg width="36" height="30" viewBox="0 0 30 24" fill="none" stroke="#fff" stroke-width="1.6"><rect x="2" y="4" width="22" height="15" rx="2"/><path d="M2 9h22"/><path d="M22 12l5 2v4c0 3-5 5-5 5"/></svg><div><b>SECURE PAYMNETS</b>QuickWallet, credit card, Bank Transfer,<br>Cash on Delivery</div></div>
</section>

<!-- Footer -->
<footer class="abs footer">
  <div class="col" style="left:120px"><h4>QUICK LINKS</h4><ul><li>Search</li><li>Become a Seller</li><li>Contact Us</li><li>Refund Policy</li><li>Shipping Policy</li><li>Privacy Policy</li><li>Terms of Service</li></ul></div>
  <div class="col" style="left:311px"><h4>MAIN MENU</h4><ul><li>Home</li><li>Decor</li><li>Gnome</li><li>Personalized Gifts</li><li>Craft Supplies</li><li>Pre-Cut Shapes</li><li>Unfinished</li><li>Wood Halloween</li></ul></div>
  <div class="col" style="left:500px;width:340px"><h4>ABOUT US</h4><p>Lorem ipsum dolor sit amet, consectetur adipiscing elit, sed do eiusmod tempor incididunt ut labore et dolore magna aliqua. Quis ipsum suspendisse ultrices gravida. Risus commodo viverra maecenas accumsan lacus vel facilisis. Lorem ipsum dolor sit amet, consectetur adipiscing elit, sed do eiusmod tempor incididunt ut labore et dolore magna aliqua</p><ul style="margin-top:8px"><li>✉ Support@Copperlantern.Com</li><li>☏ 888 888 8888</li></ul></div>
  <div class="col" style="left:882px;width:210px"><h4>NEWS &amp; UPDATES</h4><ul><li>Sign up to get the latest on</li><li>sales, new releases and more …</li></ul><div class="mail">Enter you email<i></i></div><div class="socials" aria-label="Social links"><i></i><i></i><i></i><i></i></div></div>
  <div class="copy">Copyright 2022 © Copper Lantern</div>
  <div class="pay" aria-label="Accepted payment methods"><i></i><i style="background:#c0392b"></i><i style="background:#2a6fb0"></i><i style="background:#1c4b8c"></i><i style="background:#666"></i></div>
</footer>

</body>
</html>
```